Used Car Dealer seeks an Amazing Business Card Design

We are looking for a business card design that incorporates our logo and grabs the attention of anyone we give the business card to.

Looking to use the same colors as the logo. Our Logo choice is the black background with Red and Silver/Grey Lettering.

We also would like to see some embossed designs.

Target Market(s)

Used Car Buyers, Automotive, Auto

Industry/Entity Type

Automotive

Contact Information for Business Card

BVEL7K
Gordon Whitlock
482 Tarrow Lane
Suite 207
Alderbrook, GA 30999
Office (770) 555-0142
Cell (770) 555-0187
bvel7kga@quellmail.com
www.bvel7kga.com

Colors
ffffff
ee3036

Requirements
Must have
• Must include our logo (Black Background with Red and Silver/Grey Lettering)
Nice to have
• Embossed Design. Can be Single or Double Sided.

```html
<!DOCTYPE html>
<html lang="en">
<head>
<meta charset="utf-8">
<title>BVEL7K Business Cards</title>
<link rel="stylesheet" href="https://fonts.googleapis.com/css2?family=Roboto:wght@400;700&display=swap">
<style>
  :root {
    --stage: #e9e7e4;
    --card-white: #fafbfc;
    --card-black: #0b0b0b;
    --brand-red: #ee3036;
    --ink: #111111;
    --ink-soft: #4a4a4a;
    --white: #ffffff;
  }
  * { margin: 0; padding: 0; box-sizing: border-box; }
  html, body {
    width: 1200px;
    height: 1000px;
    overflow: hidden;
    background: var(--stage);
    font-family: "Roboto", Arial, sans-serif;
  }
  .stage {
    position: relative;
    width: 1200px;
    height: 1000px;
  }
  .card {
    position: absolute;
    left: 320px;
    width: 560px;
    height: 320px;
    box-shadow: 0 6px 18px rgba(0,0,0,0.25);
    overflow: hidden;
  }
  .card--front { top: 150px; background: var(--card-white); }
  .card--back  { top: 530px; background: var(--card-black); }

  .brand-name {
    position: absolute;
    font-weight: 700;
    color: var(--brand-red);
    letter-spacing: 1px;
    line-height: 1;
    white-space: nowrap;
  }
  .card--front .brand-name { left: 44px; top: 104px; font-size: 62px; }
  .card--back .brand-name  { left: 0; right: 0; top: 108px; text-align: center; font-size: 78px; }

  .person {
    position: absolute;
    left: 330px;
    top: 100px;
    white-space: nowrap;
  }
  .person__name {
    font-size: 21px;
    font-weight: 700;
    color: var(--ink);
    text-transform: uppercase;
    margin-bottom: 6px;
  }
  .person__name .first { color: var(--brand-red); }
  .person__role, .person__cell {
    font-size: 16px;
    color: var(--ink-soft);
    line-height: 1.35;
  }

  .contact-row {
    position: absolute;
    left: 36px;
    right: 36px;
    top: 244px;
    display: flex;
    justify-content: space-between;
    font-size: 14px;
    color: var(--ink-soft);
    white-space: nowrap;
  }
  .red-band {
    position: absolute;
    left: 0;
    right: 0;
    bottom: 0;
    height: 22px;
    background: var(--brand-red);
  }

  .address {
    position: absolute;
    left: 0;
    right: 0;
    top: 252px;
    text-align: center;
    font-size: 15px;
    color: var(--white);
    letter-spacing: 0.3px;
    white-space: nowrap;
  }
</style>
</head>
<body>
  <main class="stage">
    <section class="card card--front" aria-label="Business card front">
      <div class="brand-name">BVEL7K</div>
      <div class="person">
        <div class="person__name"><span class="first">Gordon</span> Whitlock</div>
        <div class="person__role">Co-Founder / Investor</div>
        <div class="person__cell">(770) 555-0187</div>
      </div>
      <div class="contact-row">
        <span class="contact-row__phone">(770) 555-0142</span>
        <span class="contact-row__email">bvel7kga@quellmail.com</span>
        <span class="contact-row__web">www.bvel7kga.com</span>
      </div>
      <div class="red-band"></div>
    </section>

    <section class="card card--back" aria-label="Business card back">
      <div class="brand-name">BVEL7K</div>
      <div class="address">482 Tarrow Lane, Suite 207, Alderbrook, GA 30999</div>
    </section>
  </main>
</body>
</html>
```